Rally 84 Training is our company name. and instruction

We provide emergency medical training for CPR (Cardiopulmonary Resuscitation) /AED (Automated External Defibrillation) , BLS (Basic Life Support, First Aid, Bloodborne Pathogens
We travel to the client, give certified (CVL) Continental Vitality League (CVL) instruction for job/industry certification in the areas listed.
CVL Kin and Neighbors noncertified instruction

Target Market(s)

Medical professionals, job required certification

Industry/Entity Type

Medical And Science

Contact Information for Business Card

Logo
Phone, email, address, website address, FB, Instagram

Font styles to use
Serif
Sans Serif

Colors
fff2fe
ff1b2f

Requirements
Must have
• Logo
Course taught: CPR (Cardiopulmonary Resuscitation)
AED (Automated External Defibrillation)
First Aid
BLS (Basic Life Support)
Bloodborne Pathogens
Offsite instruction - we come to you
Nice to have
• Red/Black scheme
Possible ecg/heart rhythm design
Should not have
• Cartoon images

```html
<!DOCTYPE html>
<html lang="en">
<head>
<meta charset="utf-8">
<title>Rally 84 Training – Business Card</title>
<link href="https://fonts.googleapis.com/css2?family=Poppins:wght@400;500;600&display=swap" rel="stylesheet">
<style>
  :root{
    --brand-red:#ec2229;
    --ring-dark:#2b2222;
    --paper:#fdfcfe;
    --ink:#1d1a1a;
    --backdrop:#1c1c1e;
    --logo-text:#fff2fe;
  }
  *{box-sizing:border-box;margin:0;padding:0}
  html,body{width:1200px;height:900px;overflow:hidden}
  body{background:var(--backdrop);font-family:'Poppins',sans-serif;color:var(--ink);
    display:flex;flex-direction:column;align-items:center;justify-content:center;gap:40px}
  .card{position:relative;width:700px;height:400px;overflow:hidden;
    box-shadow:0 14px 30px rgba(0,0,0,.55)}
  .card--front{background:var(--paper)}
  .card--back{background:var(--brand-red)}

  .logo{position:absolute;border-radius:50%;background:var(--brand-red);
    border:7px solid var(--ring-dark);display:flex;align-items:center;justify-content:center;text-align:center}
  .logo__name{font-family:'Poppins',sans-serif;font-weight:600;color:var(--logo-text);
    font-size:30px;line-height:1.15;letter-spacing:.5px}
  .card--front .logo{left:110px;top:60px;width:220px;height:220px;box-shadow:0 0 0 3px var(--paper),0 0 0 4px rgba(0,0,0,.08)}
  .card--back .logo{left:40px;top:80px;width:240px;height:240px}
  .card--back .logo__name{font-size:32px}

  .divider{position:absolute;left:380px;top:70px;width:1.5px;height:235px;background:#555}

  .contact{position:absolute;left:400px;top:78px;font-size:15px;line-height:1.45}
  .contact__address{margin-bottom:8px}
  .contact__list{list-style:none}
  .contact__item{display:flex;align-items:center;gap:10px;margin-bottom:3px}
  .contact__icon{width:20px;height:20px;flex:none}

  .ecg-line{position:absolute;left:0;top:250px;width:700px;height:120px}

  .courses{position:absolute;left:305px;top:90px;list-style:none;font-size:15px;line-height:1}
  .courses__item{display:flex;align-items:center;gap:10px;height:38px;color:var(--ink)}
  .courses__pulse{width:26px;height:16px;flex:none}
</style>
</head>
<body>

<section class="card card--front" aria-label="Business card front">
  <div class="logo"><span class="logo__name">Rally 84<br>Training</span></div>
  <div class="divider"></div>

  <div class="contact">
    <p class="contact__address">418 Harbor Crest Lane<br>Suite 200, Millbrook<br>MI 49011</p>
    <ul class="contact__list">
      <li class="contact__item">
        <svg class="contact__icon" viewBox="0 0 20 20"><circle cx="10" cy="10" r="10" fill="var(--brand-red)"/><path d="M6.5 5.5l2 0 .8 2.2-1.2 1a6 6 0 0 0 3.2 3.2l1-1.2 2.2.8v2a1 1 0 0 1-1 1A8 8 0 0 1 5.5 6.5a1 1 0 0 1 1-1z" fill="#fff"/></svg>
        <span>61 470 628 193</span>
      </li>
      <li class="contact__item">
        <svg class="contact__icon" viewBox="0 0 20 20"><circle cx="10" cy="10" r="10" fill="var(--brand-red)"/><rect x="5" y="6.5" width="10" height="7" fill="none" stroke="#fff" stroke-width="1.3"/><path d="M5 6.8l5 4 5-4" fill="none" stroke="#fff" stroke-width="1.3"/></svg>
        <span>info@rally84training.com</span>
      </li>
      <li class="contact__item">
        <svg class="contact__icon" viewBox="0 0 20 20"><circle cx="10" cy="10" r="10" fill="var(--brand-red)"/><g fill="none" stroke="#fff" stroke-width="1.1"><circle cx="10" cy="10" r="5"/><ellipse cx="10" cy="10" rx="2.2" ry="5"/><path d="M5 10h10"/></g></svg>
        <span>www.rally84training.com</span>
      </li>
      <li class="contact__item">
        <svg class="contact__icon" viewBox="0 0 20 20"><circle cx="10" cy="10" r="10" fill="var(--brand-red)"/></svg>
        <span>@rally84training</span>
      </li>
      <li class="contact__item">
        <svg class="contact__icon" viewBox="0 0 20 20"><circle cx="10" cy="10" r="10" fill="var(--brand-red)"/></svg>
        <span>rally84training</span>
      </li>
    </ul>
  </div>

  <svg class="ecg-line" viewBox="0 0 700 120" aria-hidden="true">
    <polyline fill="none" stroke="var(--brand-red)" stroke-width="2.2" stroke-linejoin="round"
      points="0,70 400,70 410,62 418,78 428,20 438,100 446,55 454,72 462,66 470,70 530,70 538,60 546,76 556,30 566,92 574,62 582,70 640,70"/>
    <circle cx="644" cy="70" r="5" fill="var(--brand-red)"/>
  </svg>
</section>

<section class="card card--back" aria-label="Business card back">
  <div class="logo"><span class="logo__name">Rally 84<br>Training</span></div>
  <ul class="courses">
    <li class="courses__item"><svg class="courses__pulse" viewBox="0 0 26 16"><polyline fill="none" stroke="var(--ink)" stroke-width="1.3" points="0,9 6,9 8,5 10,13 13,1 16,15 18,8 20,9 26,9"/></svg>CPR (Cardiopulmonary Resuscitation)</li>
    <li class="courses__item"><svg class="courses__pulse" viewBox="0 0 26 16"><polyline fill="none" stroke="var(--ink)" stroke-width="1.3" points="0,9 6,9 8,5 10,13 13,1 16,15 18,8 20,9 26,9"/></svg>AED (Automated External Defibrillation)</li>
    <li class="courses__item"><svg class="courses__pulse" viewBox="0 0 26 16"><polyline fill="none" stroke="var(--ink)" stroke-width="1.3" points="0,9 6,9 8,5 10,13 13,1 16,15 18,8 20,9 26,9"/></svg>First Aid</li>
    <li class="courses__item"><svg class="courses__pulse" viewBox="0 0 26 16"><polyline fill="none" stroke="var(--ink)" stroke-width="1.3" points="0,9 6,9 8,5 10,13 13,1 16,15 18,8 20,9 26,9"/></svg>BLS (Basic Life Support)</li>
    <li class="courses__item"><svg class="courses__pulse" viewBox="0 0 26 16"><polyline fill="none" stroke="var(--ink)" stroke-width="1.3" points="0,9 6,9 8,5 10,13 13,1 16,15 18,8 20,9 26,9"/></svg>Bloodborne Pathogens</li>
    <li class="courses__item"><svg class="courses__pulse" viewBox="0 0 26 16"><polyline fill="none" stroke="var(--ink)" stroke-width="1.3" points="0,9 6,9 8,5 10,13 13,1 16,15 18,8 20,9 26,9"/></svg>Offsite instruction - we come to you</li>
  </ul>
</section>

</body>
</html>
```